Animal care facility (Pet Grooming, Doggie daycare, Boarding, Pet Boutique)

Hi there! i came across your wonderful work and would love to work with you! I have a clear image in my head that i want for my bussiness card and stationary. I will go ahead and attach pictures of business cards that i have found to give you an idea of what i would like to see.

My color scheme is a gray back ground and white lettering. So for the card i would like it to be a gray and the logo on the front to be white and done like picture #1. I would like the quality of the card to be a thicker more durable look. I would want just my logo and then underneath my name ( Marisa Thornquist and my title Owner similar to picture #1. I also have somone i am working with so his would need to be (Leon Vasquez, General Manager)

Also there is certain information that does need to be on the back of the card so I don't know if a white back with gray lettering would help it be easily read or not.

Halvering Pet Haven & Spa LLC
527 E. Larkmoor St.
555.204.6173 -Phone
555.208.3941-Fax
Info@halveringpethavenandspa.example-Email

Grooming- Boarding-Daycare-Pet Boutique

$10.00 OFF First Time Grooming Visit

The font for all of this is using (oranienbaum)
next to the phone fax, email I would like the actual small pictures that I have in one of the photos
Updates

Industry/Entity Type

Pet Care

Requirements
Must have
• Please follow the design of picture 7 I would like to change the direction of the card all together now. I would like the image to be up top and the name and title to be laid out the same and also in the same font as the attached picture. Again I would like all of this on the front to be engraved In white foil on gray matte backing and if we could lighten the color of this card up I would appreciate it but be on the darker side.
• On the back side keep the version you made and flip all the information to be laid out vertically just like the front.

```html
<!DOCTYPE html>
<html lang="en">
<head>
<meta charset="utf-8">
<title>Halvering Pet Haven &amp; Spa — Business Card</title>
<link rel="stylesheet" href="https://fonts.googleapis.com/css2?family=Oranienbaum&family=Courier+Prime&display=swap">
<style>
  :root {
    --stage: #e8e5e1;
    --card-gray: #6a6a6a;
    --card-gray-dark: #5d5d5d;
    --foil: #f2f2f2;
    --foil-soft: #d9d9d9;
    --paper: #ffffff;
    --ink: #4a4a4a;
    --ink-soft: #7a7a7a;
    --rule: #bdbdbd;
  }
  * { box-sizing: border-box; margin: 0; padding: 0; }
  html, body { width: 1200px; height: 812px; overflow: hidden; }
  body {
    background: var(--stage);
    font-family: "Oranienbaum", serif;
    display: flex;
    align-items: center;
    justify-content: center;
    gap: 90px;
  }
  .card {
    width: 360px;
    height: 620px;
    border-radius: 22px;
    position: relative;
    box-shadow: 0 10px 30px rgba(0,0,0,0.18);
  }

  /* Front */
  .card-front {
    background: linear-gradient(160deg, var(--card-gray) 0%, var(--card-gray-dark) 100%);
    color: var(--foil);
    display: flex;
    flex-direction: column;
    align-items: center;
    padding-top: 120px;
    text-align: center;
  }
  .brand-mark {
    width: 92px; height: 92px;
    border: 2px solid var(--foil);
    border-radius: 50%;
    margin-bottom: 28px;
  }
  .brand-name {
    font-size: 40px;
    letter-spacing: 2px;
    line-height: 1.05;
    text-transform: uppercase;
  }
  .brand-rule {
    width: 150px; height: 1px;
    background: var(--foil-soft);
    margin: 22px 0 20px;
  }
  .services {
    font-size: 13px;
    letter-spacing: 1.6px;
    text-transform: uppercase;
    color: var(--foil-soft);
  }

  /* Back */
  .card-back {
    background: var(--paper);
    color: var(--ink);
    padding: 48px 38px 0 40px;
  }
  .back-brand {
    display: flex;
    align-items: center;
    gap: 10px;
    font-size: 15px;
    letter-spacing: 1px;
    text-transform: uppercase;
    color: var(--ink);
    margin-bottom: 46px;
  }
  .back-brand .dot {
    width: 22px; height: 22px;
    border: 1.5px solid var(--ink);
    border-radius: 50%;
  }
  .person-name {
    font-size: 26px;
    letter-spacing: 1.5px;
    text-transform: uppercase;
  }
  .person-title {
    font-size: 13px;
    letter-spacing: 2px;
    text-transform: uppercase;
    color: var(--ink-soft);
    margin-top: 4px;
  }
  .contact-list {
    list-style: none;
    margin-top: 34px;
    border-left: 1px solid var(--rule);
    padding-left: 16px;
  }
  .contact-list li {
    display: flex;
    align-items: center;
    gap: 12px;
    font-size: 15px;
    line-height: 1;
    margin-bottom: 16px;
    color: var(--ink);
  }
  .contact-list svg {
    width: 15px; height: 15px;
    flex: none;
    fill: none;
    stroke: var(--ink);
    stroke-width: 1.6;
    stroke-linecap: round;
    stroke-linejoin: round;
  }
  .offer {
    position: absolute;
    left: 0; right: 0; bottom: 34px;
    text-align: center;
    font-family: "Courier Prime", monospace;
    font-size: 12px;
    letter-spacing: 2.5px;
    text-transform: uppercase;
    color: var(--ink);
  }
</style>
</head>
<body>

  <section class="card card-front" aria-label="Card front">
    <div class="brand-mark"></div>
    <h1 class="brand-name">Halvering Pet<br>Haven &amp; Spa</h1>
    <div class="brand-rule"></div>
    <p class="services">Grooming · Boarding · Daycare · Pet Boutique</p>
  </section>

  <section class="card card-back" aria-label="Card back">
    <div class="back-brand"><span class="dot"></span>Halvering Pet Haven &amp; Spa</div>

    <h2 class="person-name">Marisa Thornquist</h2>
    <p class="person-title">Owner</p>

    <ul class="contact-list">
      <li>
        <svg viewBox="0 0 16 16" aria-hidden="true"><path d="M8 15s5-5 5-8.5A5 5 0 0 0 3 6.5C3 10 8 15 8 15z"/><circle cx="8" cy="6.5" r="1.8"/></svg>
        527 E. Larkmoor St.
      </li>
      <li>
        <svg viewBox="0 0 16 16" aria-hidden="true"><path d="M3 2h3l1.5 3.5-2 1.2a8 8 0 0 0 3.8 3.8l1.2-2L14 10v3a1 1 0 0 1-1 1A12 12 0 0 1 2 3a1 1 0 0 1 1-1z"/></svg>
        555.204.6173
      </li>
      <li>
        <svg viewBox="0 0 16 16" aria-hidden="true"><rect x="2" y="6" width="12" height="7" rx="1"/><path d="M4.5 6V2h7v4M5 10h6"/></svg>
        555.208.3941
      </li>
      <li>
        <svg viewBox="0 0 16 16" aria-hidden="true"><rect x="1.5" y="3.5" width="13" height="9" rx="1"/><path d="M2 4l6 5 6-5"/></svg>
        Info@halveringpethavenandspa.example
      </li>
      <li>
        <svg viewBox="0 0 16 16" aria-hidden="true"><circle cx="8" cy="8" r="6.5"/><path d="M1.5 8h13M8 1.5c2 2 2.8 4 2.8 6.5S10 12.5 8 14.5M8 1.5C6 3.5 5.2 5.5 5.2 8S6 12.5 8 14.5"/></svg>
        www.halveringpethavenandspa.example
      </li>
    </ul>

    <p class="offer">$10.00 off first time grooming visit</p>
  </section>

</body>
</html>
```